Vacation/Holiday Home Wordpress Website

I currently have a website for our vacation/holiday rental home. It is 6 years old and needs a complete redesign to acommodate many new features available today. The existing website can be seen at www.coralbaystayrentals.co.uk . The purpose of the website is mainly to provide useful infomation about our home, the destination of Barbados. The customer is also able to check availability and book. Please note that there is a booking element to the website which is hosted externally. This can be seen at

http://stays.reservo-planner.net/PickArrival_Slim.asp?ref=kWT%3DHJRN%26QWT%3DMPLL

I now wish to add key functionality such as:

- Video of property and area
- Customer video testimonials
- Other useful information

The navigation, menus and buttons need to be re designed to give a modern, innovative and professional look and feel.

My customers are mainly females between the ages of 35 and 55. The website needs to reassure customers who are parting with a lot of mony by booking online. It needs to give a sense of trust as this may be a once in a lifetime trip which they have saved up for for a long time. Many visitors to the website will be referred by other websites such as www.nestroam.co.uk and www.villatrove.co.uk.
Updates

Dear designers, 

Thank you for taking the time to write some further comments to you all. 

1. The homepage should have an availability search function as a key feature

2. The look and feel does NOT need to have the 3 feature columns like my current website has

3.  There should not be too much text on the homepage. Brief text can be included with 'more'  buttons to reveal more information 

4.  For designs that are under consideration, we will need to see a design for the other pages as they will be different to the homepage. Information from other pages on the existing website can be used. 

Reason: Dear all, I will be providing extensive feedback later today following a review that we have conducted with a group of our guests. To enable you to read and use this information, we have extended the deadline by 5 days. Thank you for the design submisions so far. We hope that the additional feedback will enable you to amend your designs appropriately. Regards Martin Fenwick

Dear all,

Thank you for your designs.  I apologise that I am unable to give detailed feedback on each and every design submitted.  I will contact you individually and indicate whether we would like you to submit any further designs.  These should take into account the feedback below.

Feedback from design review group

1.  Logo should not be displayed in a white box.  It should blend in with the background or be overlayed onto the picture.

2.  There must be an availability calendar on the home page.

3.  Any background image should be subtle, maybe blurred and not distract from the main area.

4.  Text should be limited to a few key words with a 'read more' button to reveal more information.

5.  A gallery/slide show should be featured in the top part of the screen

6.  Icons can be used as navigation buttons

7.  Video testimonials is a key feature and should appear on the home page

8.   The use of bold and vibrant colours is preferred

9.   The 3 column format of the old website should not be copied

Regards

Martin

Target Market(s)

Female's, Families, 35 to 55 year olds, travellers to Barbados

Industry/Entity Type

Online

Requirements
Must have
• Pictures
Video
Testimonials
Clear and stylish navigation
Easy to use navigation
Should not have
• Dated look or feel

```html
<!DOCTYPE html>
<html lang="en">
<head>
<meta charset="utf-8">
<title>Coral Bay Stay Rentals – Barbados</title>
<link href="https://fonts.googleapis.com/css2?family=Oswald:wght@300;400;500&family=Open+Sans:wght@400;600&display=swap" rel="stylesheet">
<style>
:root{
  --orange:#fbaa00;
  --orange-soft:#f7c77a;
  --ink:#222222;
  --text:#333333;
  --muted:#555555;
  --line:#9a9a9a;
  --white:#ffffff;
  --dark:#3a3a3a;
}
*{box-sizing:border-box;margin:0;padding:0}
html,body{width:1025px;height:1200px;overflow:hidden;background:var(--white)}
body{font-family:"Open Sans",Arial,sans-serif;color:var(--text)}
.page{position:relative;width:1025px;height:1200px}
.abs{position:absolute}
.heading{font-family:"Oswald",Arial,sans-serif;font-weight:400;text-transform:uppercase;color:var(--ink)}

/* brand */
.brand{left:53px;top:38px;width:130px;text-align:center}
.brand-name{font-family:"Oswald",Arial,sans-serif;font-size:17px;letter-spacing:2px;color:#d8352a;font-weight:400;line-height:1.1}
.brand-mark{display:block;margin:0 auto 4px;width:14px;height:14px;border-radius:50%;background:#d8352a}

/* nav */
.main-nav{left:53px;top:131px;width:118px;list-style:none}
.main-nav li{font-family:"Oswald",Arial,sans-serif;font-size:13px;color:var(--ink);height:25.6px;line-height:22px;border-bottom:1px dashed var(--line)}
.follow{left:53px;top:330px;font-family:"Oswald",Arial,sans-serif;font-size:10px;color:var(--ink)}
.social{left:54px;top:351px;display:flex;gap:3px}
.social span{width:20px;height:20px;background:var(--orange)}
.follow-bar{left:54px;top:378px;width:118px;height:4px;background:var(--orange-soft)}
.follow-bar::before{content:"";position:absolute;left:0;top:0;width:46px;height:4px;background:var(--orange)}

/* hero */
.hero{left:216px;top:19px;width:593px;height:397px;background:linear-gradient(180deg,#5b9be0 0%,#b9d7f2 38%,#56b6c4 62%,#2aa1ad 80%,#c9e6e0 100%)}
.hero-arrow{top:176px;width:50px;height:88px;background:rgba(255,255,255,.28);display:flex;align-items:center;justify-content:center}
.hero-arrow.prev{left:0}.hero-arrow.next{right:0}
.hero-caption{left:0;bottom:0;width:100%;height:100px;background:rgba(255,255,255,.35);padding:18px 32px}
.hero-title{font-size:17px;color:var(--ink);letter-spacing:.2px}
.hero-text{font-size:11px;color:var(--ink);margin-top:3px}
.btn{display:inline-block;background:var(--orange);font-family:"Oswald",Arial,sans-serif;text-transform:uppercase;color:var(--ink);font-size:11px}
.hero .btn{margin-top:12px;width:80px;height:21px;line-height:21px;text-align:center}

/* side widgets */
.widget{left:824px;width:167px}
.widget-band{position:absolute;left:0;bottom:0;width:100%;background:var(--orange);text-align:center;padding-top:3px}
.widget-band .title{font-family:"Oswald",Arial,sans-serif;font-size:17px;color:var(--white);text-transform:uppercase;line-height:22px}
.widget-band .sub{margin:2px 8px 0;border-top:1px dashed rgba(255,255,255,.8);font-size:7px;font-weight:600;color:var(--ink);text-transform:uppercase;text-align:left;padding:3px 6px;display:flex;justify-content:space-between;align-items:center}
.dot{width:7px;height:7px;border-radius:50%;background:var(--white)}
.climate{top:19px;height:121px;background:linear-gradient(180deg,#7fa8c8,#3d6f8a)}
.weather{position:absolute;left:11px;top:6px;width:144px;height:64px;background:rgba(235,240,243,.92);padding:8px 12px;font-size:16px;color:var(--ink)}
.weather small{display:block;font-size:8px}
.weather .search{position:absolute;left:12px;bottom:6px;width:120px;height:11px;background:#4fa6b4;border-radius:3px;font-size:7px;color:var(--white);padding-left:26px;line-height:11px}
.video{top:157px;height:122px;border-top:8px solid var(--dark)}
.video-screen{position:absolute;left:0;top:0;width:100%;height:69px;background:linear-gradient(180deg,#6a95b8,#c9b99a 60%,#8a7d5a)}
.player{position:absolute;left:0;width:100%;height:9px;background:var(--dark);font-size:6px;color:var(--white);padding-left:32px;line-height:9px}
.booking{top:295px;height:122px;border:1px solid #cccccc;background:var(--white)}
.booking form{padding:5px 8px;font-size:8px;color:var(--ink)}
.field-row{display:flex;align-items:center;height:17px}
.field-row label{width:54px;text-transform:uppercase}
.field{width:78px;height:12px;border:1px solid #bbbbbb;color:#aaaaaa;font-size:7.5px;padding-left:6px;line-height:10px}
.cal{width:11px;height:11px;margin-left:5px;background:#e98b4a;border:1px solid #999999}
.book-now{display:block;margin-top:3px;width:118px;height:11px;background:#9a9a9a;color:var(--white);font-size:7px;text-align:center;line-height:11px}

/* about */
.about-head{left:53px;top:457px;width:132px;text-align:center;font-size:13px}
.about-text{left:54px;top:496px;width:128px;font-size:8.3px;line-height:12.3px;color:var(--ink)}
.about-rule{left:186px;top:496px;width:3px;height:176px;background:var(--orange)}

/* features */
.feature{width:241px;top:446px;text-align:center}
.feature .heading{font-size:13px;height:37px}
.feature-media{width:241px;height:164px}
.feature .caption{font-family:"Oswald",Arial,sans-serif;font-weight:300;font-size:14.5px;color:#555555;margin-top:6px;text-transform:uppercase;letter-spacing:.3px}

/* galleries */
.section-title{left:30px;top:711px;width:965px;display:flex;align-items:center;gap:24px;font-size:13px}
.section-title::before,.section-title::after{content:"";flex:1;border-top:2px solid #555555;border-bottom:1px solid #aaaaaa;height:3px}
.tile{width:232px}
.tile-media{width:232px;height:148px}
.tile-label{display:flex;align-items:center;height:29px;margin-top:1px}
.tile-icon{width:29px;height:29px;background:var(--orange);display:flex;align-items:center;justify-content:center;flex:none}
.tile-label .heading{font-size:13px;margin-left:15px;letter-spacing:.3px;white-space:nowrap}

.footer{left:0;top:1176px;width:1025px;height:24px;background:var(--orange);font-size:8px;color:var(--white);padding:0 31px;display:flex;justify-content:space-between;align-items:center}
.footer-rule{left:0;top:1171px;width:1025px;border-top:2px solid #444444}
</style>
</head>
<body>
<div class="page">

  <div class="abs brand"><span class="brand-mark"></span><div class="brand-name">CORAL BAY STAY RENTALS</div></div>

  <ul class="abs main-nav">
    <li>HOME</li><li>ABOUT BARBADOS</li><li>VIDEOS</li><li>TESTIMONIALS</li><li>BOOIKNG</li><li>EVENTS</li><li>CONTACT</li>
  </ul>
  <div class="abs follow">Follow</div>
  <div class="abs social" aria-label="Social links"><span></span><span></span><span></span><span></span><span></span></div>
  <div class="abs follow-bar"></div>

  <section class="abs hero">
    <div class="abs" style="inset:0" role="img" aria-label="Marina with yachts, turquoise water and a sunny sky"></div>
    <div class="abs hero-arrow prev"><svg width="14" height="30" viewBox="0 0 14 30"><path d="M12 2 2 15l10 13" fill="none" stroke="#fff" stroke-width="1.5"/></svg></div>
    <div class="abs hero-arrow next"><svg width="14" height="30" viewBox="0 0 14 30"><path d="M2 2l10 13L2 28" fill="none" stroke="#fff" stroke-width="1.5"/></svg></div>
    <div class="abs hero-caption">
      <h1 class="heading hero-title">Nemo enim ipsam voluptatem quia volptas sit aspernatur</h1>
      <p class="hero-text">Lorem ipsum dolor sit amet, consectetur adipisicing elit.</p>
      <span class="btn">Read more</span>
    </div>
  </section>

  <aside class="abs widget climate">
    <div class="weather">32°<small>Cloudy</small>
      <svg class="abs" style="right:14px;top:8px" width="40" height="30" viewBox="0 0 40 30"><path d="M10 26a7 7 0 0 1 1-14 9 9 0 0 1 17 2 6 6 0 0 1 0 12z" fill="none" stroke="#555" stroke-width="1.5"/></svg>
      <div class="search">Barbados</div>
    </div>
    <div class="widget-band"><div class="title">Climate</div><div class="sub">Whatever time of year you visit<span class="dot"></span></div></div>
  </aside>

  <aside class="abs widget video">
    <div class="video-screen" role="img" aria-label="Villa exterior video frame"></div>
    <div class="player" style="top:69px">0:00 / 2:54</div>
    <div class="widget-band"><div class="title">Property video</div><div class="sub">Marisol: a 2 bedroomed, fully<span class="dot"></span></div></div>
  </aside>

  <aside class="abs widget booking">
    <form>
      <div class="field-row"><label>Check in</label><span class="field">DD/MM/YY</span><span class="cal"></span></div>
      <div class="field-row"><label>Check out</label><span class="field">DD/MM/YY</span><span class="cal"></span></div>
      <div class="field-row"><label>Guests</label><span class="field"></span></div>
      <span class="book-now">BOOK NOW</span>
    </form>
    <div class="widget-band"><div class="title">Check availability</div><div class="sub">Providing you the best service<span class="dot"></span></div></div>
  </aside>

  <h2 class="abs heading about-head">– About Barbados –</h2>
  <p class="abs about-text">Lorem ipsum dolor sit amet, consectetur adipisicing elit, sed do eiusmod tempor incididunt ut labore et dolore magna aliqua. Ut enim ad minim veniam, quis nostrud exercitation ullamco laboris nisi ut aliquip ex ea commodo consequat. Duis aute irure dolor in reprehenderit in voluptate velit esse cillum dolore eu fugiat nulla pariatur. Excepteur sint occaecat cupidatat non proident, sunt in culpa qui officia</p>
  <div class="abs about-rule"></div>

  <article class="abs feature" style="left:216px"><h3 class="heading">Destination Barbados</h3><div class="feature-media" style="background:linear-gradient(135deg,#b6cfe9,#e9e6da 50%,#cdd9b8)" role="img" aria-label="Road map of the island"></div><p class="caption">Lorem ipsum dolor sit</p></article>
  <article class="abs feature" style="left:483px"><h3 class="heading">Events of Barbados</h3><div class="feature-media" style="background:linear-gradient(180deg,#8a7a6a,#d9a630 55%,#8f8b86)" role="img" aria-label="Carnival dancers in yellow costumes"></div><p class="caption">Lorem ipsum dolor sit</p></article>
  <article class="abs feature" style="left:751px"><h3 class="heading">Cuisines of Barbados</h3><div class="feature-media" style="background:radial-gradient(circle at 50% 55%,#e0a35a,#f1eadf 55%,#8c2a22)" role="img" aria-label="Plate of fried fish with macaroni pie"></div><p class="caption">Lorem ipsum dolor sit</p></article>

  <h2 class="abs heading section-title">Image galleries</h2>

  <div class="abs tile" style="left:30px;top:753px"><div class="tile-media" style="background:linear-gradient(180deg,#3fa9c9,#1b6f92)" role="img" aria-label="Submarine over a coral reef"></div><div class="tile-label"><span class="tile-icon"><svg width="12" height="10"><rect x=".5" y=".5" width="11" height="9" fill="none" stroke="#fff"/><path d="M2 8l3-4 2 2 1-1 2 3z" fill="#fff"/></svg></span><h3 class="heading">Reefline Submarines</h3></div></div>
  <div class="abs tile" style="left:275px;top:753px"><div class="tile-media" style="background:linear-gradient(180deg,#3a2a1c,#a07a4a 50%,#2a1e14)" role="img" aria-label="Limestone cave with a pool"></div><div class="tile-label"><span class="tile-icon"><svg width="12" height="10"><rect x=".5" y=".5" width="11" height="9" fill="none" stroke="#fff"/><path d="M2 8l3-4 2 2 1-1 2 3z" fill="#fff"/></svg></span><h3 class="heading">Limestone Hollow Cave</h3></div></div>
  <div class="abs tile" style="left:520px;top:753px"><div class="tile-media" style="background:linear-gradient(135deg,#4f7a2a,#1f3a14)" role="img" aria-label="Monkeys in a forest"></div><div class="tile-label"><span class="tile-icon"><svg width="12" height="10"><rect x=".5" y=".5" width="11" height="9" fill="none" stroke="#fff"/><path d="M2 8l3-4 2 2 1-1 2 3z" fill="#fff"/></svg></span><h3 class="heading">Coral Wildlife Reserve</h3></div></div>
  <div class="abs tile" style="left:764px;top:753px"><div class="tile-media" style="background:linear-gradient(180deg,#3f8ad6,#cfe4f4 55%,#2a9fb8)" role="img" aria-label="Motor yacht on open sea"></div><div class="tile-label"><span class="tile-icon"><svg width="12" height="10"><rect x=".5" y=".5" width="11" height="9" fill="none" stroke="#fff"/><path d="M2 8l3-4 2 2 1-1 2 3z" fill="#fff"/></svg></span><h3 class="heading">The Tide Keeper</h3></div></div>

  <div class="abs tile" style="left:30px;top:963px"><div class="tile-media" style="background:linear-gradient(180deg,#3a3a3a 0 8%,#e8e0d6 8% 50%,#b88a6a 50% 90%,#3a3a3a 90%)" role="img" aria-label="Guest testimonial video frame"></div><div class="tile-label"><span class="tile-icon"><svg width="12" height="10"><rect x=".5" y=".5" width="11" height="9" fill="none" stroke="#fff"/><path d="M2 8l3-4 2 2 1-1 2 3z" fill="#fff"/></svg></span><h3 class="heading">Testimonial video</h3></div></div>
  <div class="abs tile" style="left:275px;top:963px"><div class="tile-media" style="background:linear-gradient(180deg,#2f5a1e,#7cb23a 55%,#4c8a24)" role="img" aria-label="Green golf course fairway"></div><div class="tile-label"><span class="tile-icon"><svg width="12" height="10"><rect x=".5" y=".5" width="11" height="9" fill="none" stroke="#fff"/><path d="M2 8l3-4 2 2 1-1 2 3z" fill="#fff"/></svg></span><h3 class="heading">Palm Ridge Golf Club</h3></div></div>
  <div class="abs tile" style="left:520px;top:963px"><div class="tile-media" style="background:linear-gradient(180deg,#7ab6e0,#2a6fa8 55%,#d8d3c4)" role="img" aria-label="Jeep tour on a coastal cliff"></div><div class="tile-label"><span class="tile-icon"><svg width="12" height="10"><rect x=".5" y=".5" width="11" height="9" fill="none" stroke="#fff"/><path d="M2 8l3-4 2 2 1-1 2 3z" fill="#fff"/></svg></span><h3 class="heading">Coastline Jeep Tours</h3></div></div>
  <div class="abs tile" style="left:764px;top:963px"><div class="tile-media" style="background:linear-gradient(180deg,#4b93d6,#46c1c4 55%,#efe3c8)" role="img" aria-label="Driftwood on a white sand beach"></div><div class="tile-label"><span class="tile-icon"><svg width="12" height="10"><rect x=".5" y=".5" width="11" height="9" fill="none" stroke="#fff"/><path d="M2 8l3-4 2 2 1-1 2 3z" fill="#fff"/></svg></span><h3 class="heading">Driftwood Cove Beach</h3></div></div>

  <div class="abs footer-rule"></div>
  <footer class="abs footer"><span>copyright © Coral Bay Stay Rentals 2013. All Rights Reserved</span><span style="color:var(--ink)">TOP</span></footer>
</div>
</body>
</html>
```